Birch Ledger brochure to showcase Masonry, landscape and concrete services

SEE RECENT COMMENT PAGE FOR BEST INFO We need a brochure designed to help inform our clients of our services and give them information on the pitfalls in the masonry, landscape and Hardscape industry, including drainage and frost protection, showcase some of our work we like to make all our material for marketing geared toward helping the client learn something. Drainage on any site is the number one component to a successful landscape, Hardscape and outdoor living area. This is often and overlooked to get to the stuff that's fun in turn, causing failure from frost due to northern Minnesota's harsh climate. Creating many disappointments on a large investment project. The brochure should also have a section focused on masonry, including fireplaces chimney repair, stucco repair, stone and brick. Some of the language should be editable. I will attach pictures and our logo.

Target Market(s)

Older customers with dual income looking to update and add outdoor living

Industry/Entity Type

Masonry, landscape, concrete, outdoor living

Font styles to use
Serif
Sans Serif
Other font styles liked:
• Arial

Colors

Designer to choose only greyscale colors for use in the design.

Requirements
Must have
• I really like gray, silver and black when I do marketing mixed with White, but I thought adding some greenery for the landscape portion might look good too on this brochure
Nice to have
• I do not like it too busy so keep it clean and simple
Should not have
• Tons of clutter, tons of words, hard to read and look at

```html
<!DOCTYPE html>
<html lang="en">
<head>
<meta charset="UTF-8">
<title>Birch Ledger – Services Brochure</title>
<link href="https://fonts.googleapis.com/css2?family=Open+Sans:wght@300;400;600;700&family=Noto+Serif:ital@1&display=swap" rel="stylesheet">
<style>
  :root{
    --charcoal:#333335;
    --ink:#232325;
    --silver:#b3b3b3;
    --silver-dark:#8c8c8c;
    --white:#ffffff;
    --text-dark:#2b2b2d;
    --photo-stone:#55585c;
    --photo-wood:#c79a6b;
  }
  *{margin:0;padding:0;box-sizing:border-box}
  html,body{width:1200px;height:1200px;overflow:hidden;background:var(--white)}
  body{font-family:"Open Sans",Arial,sans-serif}
  .canvas{position:relative;width:1200px;height:1200px;overflow:hidden;background:var(--white)}
  .abs{position:absolute}

  .sheet{position:absolute;left:197px;width:805px;height:569px;background:var(--white);overflow:hidden;box-shadow:0 6px 14px rgba(0,0,0,.35)}
  .sheet-outside{top:18px}
  .sheet-inside{top:614px}

  /* Outside sheet */
  .services-band{left:0;top:0;width:203px;height:569px;background:var(--charcoal);border-radius:0 14px 14px 0}
  .service-card{left:58px;width:198px;height:117px;background:var(--silver);border-radius:16px}
  .service-photo{left:58px;width:90px;height:90px;border-radius:0 18px 0 0;border:1.5px solid var(--white)}
  .service-number{left:163px;font-size:32px;font-weight:300;color:var(--white);line-height:1}
  .service-copy{left:72px;width:172px;font-size:9.2px;line-height:14px;color:var(--white)}

  .about-panel{left:280px;top:0;width:245px;height:569px;background:var(--charcoal);border-radius:20px 0 20px 20px}
  .about-tab{left:375px;top:0;width:150px;height:132px;background:var(--silver);border-radius:0 0 22px 0}
  .about-photo{left:303px;width:198px;height:105px;border-radius:16px;border:1.5px solid var(--white)}
  .about-title{left:303px;top:340px;font-size:26px;font-weight:700;color:var(--white)}
  .about-copy{left:303px;width:198px;font-size:9.9px;line-height:14px;color:var(--white);text-align:justify}

  .brand{left:555px;top:30px;width:250px;text-align:center}
  .brand-mark{width:36px;height:36px;border-radius:50%;background:var(--silver-dark);margin:0 auto 8px}
  .brand-name{font-size:15px;font-weight:400;letter-spacing:3px;color:var(--text-dark);text-transform:uppercase}
  .brand-tagline{font-size:6px;font-weight:600;letter-spacing:1.6px;color:var(--text-dark);margin-top:4px}
  .cover-block{left:629px;top:140px;width:176px;height:253px;background:var(--silver);border-radius:60px 0 0 0}
  .cover-photo{left:555px;top:168px;width:190px;height:362px;border-radius:0 95px 0 60px;background:linear-gradient(180deg,var(--photo-wood) 0%,#a88462 30%,var(--photo-stone) 45%,#3e4043 85%,#2e3033 100%)}

  .dot-field{background:rgba(60,60,62,.08)}

  /* Inside sheet */
  .checklist-panel{left:0;top:0;width:283px;height:569px;background:var(--charcoal)}
  .check{left:64px;width:56px;height:56px}
  .check-label{left:149px;width:112px;font-size:15.5px;font-weight:700;line-height:19px;color:var(--silver)}

  .gallery-panel{left:283px;top:0;width:242px;height:569px;background:var(--silver)}
  .gallery-photo{left:280px;top:0;width:245px;height:212px;border-radius:0 0 50% 50% / 0 0 52% 52%;background:linear-gradient(180deg,#7fa4c9 0%,#9eb6c6 25%,#4c5a3a 45%,#7a5a45 70%,#6a6a62 100%)}
  .contact-card{left:303px;top:284px;width:198px;height:261px;background:var(--ink);border-radius:18px;padding:48px 17px 0 17px;color:var(--white)}
  .contact-title{font-size:18.5px;font-weight:700;margin-bottom:12px}
  .contact-row{display:flex;align-items:flex-start;gap:9px;font-size:10px;line-height:14px;margin-bottom:9px}
  .contact-row svg{flex:0 0 18px;width:18px;height:18px;margin-top:-2px}

  .who-photo{left:550px;top:0;width:253px;height:366px;border-radius:0 0 0 115px;background:linear-gradient(160deg,#8a8378 0%,#5a3e2e 30%,#4a3325 65%,#5d4a36 100%)}
  .who-pill{left:582px;top:352px;width:158px;height:34px;background:var(--silver);border-radius:17px;text-align:center;font-size:17px;font-weight:700;line-height:34px;color:var(--text-dark)}
  .who-copy{left:549px;top:400px;width:228px;font-family:"Noto Serif",Georgia,serif;font-style:italic;font-size:9.9px;line-height:14.4px;color:var(--text-dark);text-align:center}
</style>
</head>
<body>
<div class="canvas">

  <section class="sheet sheet-outside">
    <div class="abs services-band"></div>

    <div class="abs service-card" style="top:70px"></div>
    <div class="abs service-photo" style="top:25px;background:linear-gradient(180deg,#7aa0cc,#9a8a7a 60%,#6d5a4c)" role="img" aria-label="Deck and sunroom addition under construction"></div>
    <div class="abs service-number" style="top:82px">01</div>
    <p class="abs service-copy" style="top:127px">Lorem ipsum dolor sit amet, consectetur adipiscing elit. Ut tempor magna erat,</p>

    <div class="abs service-card" style="top:249px"></div>
    <div class="abs service-photo" style="top:204px;background:linear-gradient(180deg,#4f6a38,#9a9288 55%,#b8a78e)" role="img" aria-label="Outdoor kitchen with stone counter"></div>
    <div class="abs service-number" style="top:259px">02</div>
    <p class="abs service-copy" style="top:305px">Lorem ipsum dolor sit amet, consectetur adipiscing elit. Ut tempor magna erat,</p>

    <div class="abs service-card" style="top:427px"></div>
    <div class="abs service-photo" style="top:382px;background:radial-gradient(circle at 50% 55%,#b0312a 0%,#3a3a3c 30%,#6c6c6c 100%)" role="img" aria-label="Round fieldstone fireplace with fire"></div>
    <div class="abs service-number" style="top:438px">03</div>
    <p class="abs service-copy" style="top:484px">Lorem ipsum dolor sit amet, consectetur adipiscing elit. Ut tempor magna erat,</p>

    <div class="abs about-panel"></div>
    <div class="abs about-tab"></div>
    <div class="abs dot-field" style="left:409px;top:25px;width:68px;height:70px" role="img" aria-label="Dotted grid accent"></div>
    <div class="abs about-photo" style="top:75px;background:linear-gradient(135deg,#6f8a3e,#5b5040 45%,#77766c)" role="img" aria-label="Stone steps through a planted garden"></div>
    <div class="abs about-photo" style="top:197px;background:linear-gradient(180deg,#c9a98a 0%,#6f7a4c 30%,#5d5140 70%,#6a6a66)" role="img" aria-label="Hillside rock garden overlooking a valley"></div>
    <h2 class="abs about-title">About Us !</h2>
    <p class="abs about-copy" style="top:386px">Lorem ipsum dolor sit amet, consectetur adipiscing elit. Ut tempor magna erat, et euismod felis lacinia quis. Proin porta sodales odio eu ultricies. Donec semper ex ac neque euismod tincidunt.</p>
    <p class="abs about-copy" style="top:470px">Quisque luctus rhoncus lorem id hendrerit. Pellentesque quis luctus augue. Maecenas in varius ipsum, non convallis sapien.</p>

    <div class="abs brand">
      <div class="brand-mark"></div>
      <div class="brand-name">Birch Ledger</div>
      <div class="brand-tagline">Built On Solid Ground</div>
    </div>
    <div class="abs cover-block"></div>
    <div class="abs dot-field" style="left:525px;top:143px;width:67px;height:67px" role="img" aria-label="Dotted grid accent"></div>
    <div class="abs cover-photo" role="img" aria-label="Stacked stone fireplace and chimney in a cedar-lined room"></div>
    <div class="abs dot-field" style="left:549px;top:477px;width:67px;height:67px" role="img" aria-label="Dotted grid accent"></div>
  </section>

  <section class="sheet sheet-inside">
    <div class="abs checklist-panel"></div>

    <svg class="abs check" style="top:30px" viewBox="0 0 56 56" aria-hidden="true"><circle cx="26" cy="30" r="22" fill="none" stroke="#b3b3b3" stroke-width="5"/><path d="M14 30 L24 42 L50 6" fill="none" stroke="#b3b3b3" stroke-width="7" stroke-linecap="round" stroke-linejoin="round"/></svg>
    <div class="abs check-label" style="top:30px">landscape and Hardscape industry</div>

    <svg class="abs check" style="top:120px" viewBox="0 0 56 56" aria-hidden="true"><circle cx="26" cy="30" r="22" fill="none" stroke="#b3b3b3" stroke-width="5"/><path d="M14 30 L24 42 L50 6" fill="none" stroke="#b3b3b3" stroke-width="7" stroke-linecap="round" stroke-linejoin="round"/></svg>
    <div class="abs check-label" style="top:120px">drainage and frost protection</div>

    <svg class="abs check" style="top:210px" viewBox="0 0 56 56" aria-hidden="true"><circle cx="26" cy="30" r="22" fill="none" stroke="#b3b3b3" stroke-width="5"/><path d="M14 30 L24 42 L50 6" fill="none" stroke="#b3b3b3" stroke-width="7" stroke-linecap="round" stroke-linejoin="round"/></svg>
    <div class="abs check-label" style="top:209px">Hardscape and outdoor living area</div>

    <svg class="abs check" style="top:297px" viewBox="0 0 56 56" aria-hidden="true"><circle cx="26" cy="30" r="22" fill="none" stroke="#b3b3b3" stroke-width="5"/><path d="M14 30 L24 42 L50 6" fill="none" stroke="#b3b3b3" stroke-width="7" stroke-linecap="round" stroke-linejoin="round"/></svg>
    <div class="abs check-label" style="top:296px;width:120px">including fireplaces chimney repair</div>

    <svg class="abs check" style="top:386px" viewBox="0 0 56 56" aria-hidden="true"><circle cx="26" cy="30" r="22" fill="none" stroke="#b3b3b3" stroke-width="5"/><path d="M14 30 L24 42 L50 6" fill="none" stroke="#b3b3b3" stroke-width="7" stroke-linecap="round" stroke-linejoin="round"/></svg>
    <div class="abs check-label" style="top:404px;width:130px">Stucco Repair</div>

    <svg class="abs check" style="top:475px" viewBox="0 0 56 56" aria-hidden="true"><circle cx="26" cy="30" r="22" fill="none" stroke="#b3b3b3" stroke-width="5"/><path d="M14 30 L24 42 L50 6" fill="none" stroke="#b3b3b3" stroke-width="7" stroke-linecap="round" stroke-linejoin="round"/></svg>
    <div class="abs check-label" style="top:485px;width:90px">Stone and Brick</div>

    <div class="abs gallery-panel"></div>
    <div class="abs gallery-photo" role="img" aria-label="Terraced stone retaining walls with evergreens and a gravel path"></div>
    <div class="abs dot-field" style="left:458px;top:251px;width:67px;height:67px" role="img" aria-label="Dotted grid accent"></div>

    <div class="abs contact-card">
      <div class="contact-title">Contact Us</div>
      <div class="contact-row">
        <svg viewBox="0 0 20 20" aria-hidden="true"><circle cx="10" cy="10" r="8.5" fill="none" stroke="#fff" stroke-width="1.2"/><path d="M7 5.5c-.8.4-1.3 1.2-1 2.3.8 2.8 2.6 4.8 5.3 6 1 .4 1.9 0 2.4-.8l-1.8-1.5-1.1.8c-1.3-.7-2.3-1.8-2.9-3.1l.8-1.1z" fill="#fff"/></svg>
        <span>+123-456-7890</span>
      </div>
      <div class="contact-row">
        <svg viewBox="0 0 20 20" aria-hidden="true"><circle cx="10" cy="10" r="9.5" fill="#fff"/><rect x="5" y="6.5" width="10" height="7" rx="1" fill="none" stroke="#232325" stroke-width="1.3"/><path d="M5.3 7 L10 10.6 L14.7 7" fill="none" stroke="#232325" stroke-width="1.3"/></svg>
        <span>hello@birchledger.com</span>
      </div>
      <div class="contact-row">
        <svg viewBox="0 0 20 20" aria-hidden="true"><g fill="none" stroke="#fff" stroke-width="1.1"><circle cx="10" cy="10" r="7.5"/><ellipse cx="10" cy="10" rx="3.3" ry="7.5"/><path d="M2.5 10h15M3.6 6.2h12.8M3.6 13.8h12.8"/></g></svg>
        <span>www.birchledger.com</span>
      </div>
      <div class="contact-row">
        <svg viewBox="0 0 20 20" aria-hidden="true"><path d="M10 3 L2.5 10 H5 V16.5 H8.5 V12.5 H11.5 V16.5 H15 V10 H17.5 Z" fill="#fff"/></svg>
        <span>123 Anywhere St., Any City, ST 12345</span>
      </div>
    </div>

    <div class="abs who-photo" role="img" aria-label="Trench with drainage pipe along a fence line"></div>
    <div class="abs dot-field" style="left:550px;top:16px;width:67px;height:68px" role="img" aria-label="Dotted grid accent"></div>
    <div class="abs who-pill">Who We are</div>
    <p class="abs who-copy">Birch Ledger builds stone, brick and landscape projects for homeowners across the northern lakes region. Every job starts with a careful site review and an honest talk about what the ground needs, so there are no surprises later. Long winters punish shortcuts, which is why we plan drainage, frost depth and runoff before anything else goes in. From patios and retaining walls to fireplaces and chimneys, our crews deliver solid work made to hold up year after year.</p>
  </section>

</div>
</body>
</html>
```